Super Greens Label for Supplement Bottle

We want to design a front label for a health supplement bottle. The product is called Meadow Twist Chews™. This will be a new product so there is no current website for the product. The focus is on supergreens that taste great and deliver support for energy, digestion, and immune defense.
We want it to be modern, vibrant and appealing.
Bottle size: standard size supplement CLEAR bottle size, with white child resistant cap and the label panel dimensions are 3” x 7”. The label should be primarily white and green, with a touch of red; (see color palettes)/it can also ONLY be white and green. See samples attached.
We are only focused on the front of the bottle design, not on the back, but leave space for the supplement panel and other text on the back.
So the text for the front of the bottle is:
RT Balden's
Meadow Twist Chews™
Super Greens Blend for:
Energy, Digestion, and Immune Support*
60 Gummies | Dietary Supplement
Raspberry Flavor Gummies
Off to side of the label:
Non-GMO
Vegan Friendly
Plant-Based
Gelatin Free
Colors
Designer to choose colors to be used in the design.

```html
<!DOCTYPE html>
<html lang="en">
<head>
<meta charset="utf-8">
<title>RT Balden's Meadow Twist Chews – Front Label</title>
<link rel="stylesheet" href="https://fonts.googleapis.com/css2?family=Montserrat:ital,wght@0,400;0,500;1,800&display=swap">
<style>
  :root {
    --backdrop: #f2d3d6;
    --label-white: #ffffff;
    --brand-green: #1b6b36;
    --brand-red: #e0262b;
    --ink: #1a1a1a;
    --berry-deep: #c81e35;
    --berry-light: #f2596b;
  }
  * { margin: 0; padding: 0; box-sizing: border-box; }
  html, body {
    width: 960px; height: 1200px; overflow: hidden;
    background: var(--backdrop);
    font-family: "Montserrat", sans-serif;
  }
  .canvas { position: relative; width: 960px; height: 1200px; }
  .label {
    position: absolute; left: 36px; top: 410px;
    width: 888px; height: 381px;
    background: var(--label-white); overflow: hidden;
  }
  .label-frame { position: absolute; inset: 0; }
  .label-text { position: absolute; white-space: nowrap; line-height: 1; }
  .centered { left: 445px; transform: translateX(-50%); }
  .maker { top: 30px; font-size: 31px; color: var(--brand-red); }
  .product-name { top: 90px; font-size: 39px; color: var(--brand-green); letter-spacing: 0.5px; }
  .product-type { top: 139px; font-size: 29px; color: var(--brand-red); letter-spacing: 0.5px; }
  .flavor { top: 189px; font-size: 19.5px; color: var(--label-white); font-weight: 500; letter-spacing: 0.3px; }
  .benefits { left: 284px; top: 236px; font-size: 14.5px; line-height: 18px; color: var(--ink); }
  .count { left: 320px; top: 284px; font-size: 56px; font-weight: 800; font-style: italic; color: var(--ink); letter-spacing: -1px; }
  .format { left: 323px; top: 338px; font-size: 15px; color: var(--ink); }
  .fruit-art {
    position: absolute; left: 472px; top: 212px; width: 128px; height: 104px;
    border-radius: 50%;
    background: radial-gradient(circle at 40% 45%, var(--berry-light), var(--berry-deep) 70%);
  }
  .claims { position: absolute; left: 30px; top: 287px; list-style: none; }
  .claims li {
    display: flex; align-items: center; gap: 5px;
    font-size: 11.5px; color: var(--ink); height: 18.5px;
  }
  .claim-dot { width: 13px; height: 13px; border-radius: 50%; flex: none; }
  .claim-dot.green { background: var(--brand-green); }
  .claim-dot.red { background: var(--brand-red); }
</style>
</head>
<body>
<main class="canvas">
  <section class="label">
    <svg class="label-frame" width="888" height="381" viewBox="0 0 888 381" aria-hidden="true">
      <defs>
        <clipPath id="inner-oval"><ellipse cx="445" cy="189" rx="189" ry="243"/></clipPath>
      </defs>
      <ellipse cx="445" cy="189" rx="202" ry="256" fill="none" stroke="var(--brand-red)" stroke-width="4.5"/>
      <ellipse cx="445" cy="189" rx="191" ry="245" fill="none" stroke="var(--brand-green)" stroke-width="5"/>
      <rect x="240" y="184" width="420" height="30" fill="var(--brand-green)" clip-path="url(#inner-oval)"/>
    </svg>

    <p class="label-text centered maker">RT Balden's</p>
    <h1 class="label-text centered product-name" style="font-weight:400">MEADOW TWIST</h1>
    <p class="label-text centered product-type">CHEWS™</p>
    <p class="label-text centered flavor">RASPBERRY FLAVOR GUMMIES</p>

    <p class="label-text benefits">Energy, Digestion,<br>and Immune Support*</p>
    <div class="fruit-art" role="img" aria-label="Illustration of ripe raspberries with green leaves"></div>
    <p class="label-text count">60</p>
    <p class="label-text format">Gummies | Dietary Supplement</p>

    <ul class="claims">
      <li><span class="claim-dot green"></span>Non-GMO</li>
      <li><span class="claim-dot red"></span>Vegan Friendly</li>
      <li><span class="claim-dot green"></span>Plant-Based</li>
      <li><span class="claim-dot red"></span>Gelatin Free</li>
    </ul>
  </section>
</main>
</body>
</html>
```